Flyer Design Project

We are a mortgage company Tamberlyn Funding Corp. that will be looking to mail out these flyers to promote Reverse Mortgages. Some clip art of Seniors (Happy Smile having a good time) Our phone number on the flyer in a few places 877-520-6184
Text: No Celebrity Endorsers or talking heads here
Solutions for seniors... Stop worrying Start Living
Say Goodby to monthly payments with a reverse mortgage
The Loan That Pays You
Secure Your Retirement With A Reverse Mortgage
GKP Goverment Insured
Retain Complete ownership of your Home
Save and Effective Financial Tool
Pay Off Credit cards Elimanate Mortgage payments improve your home or lifestyle
No Credit score or income requirements
Faceing a foreclosure a reverse mortgage can help
Is a reverse mortgage right for you? Get the facts from a qualified reverse mortgage originator
The text above does not have to be in that order
I am having trouble with my Logo so i am getting a new file and will be able to upload it to the flyer shortly just leave room for it
Seniors over the age of 62
Financial

```html
<!DOCTYPE html>
<html lang="en">
<head>
<meta charset="utf-8">
<title>Tamberlyn Funding Corp. – Reverse Mortgage Flyer</title>
<link rel="stylesheet" href="https://fonts.googleapis.com/css2?family=Arimo:wght@400;700&family=PT+Serif:wght@400&display=swap">
<style>
  :root {
    --green: #8cc63f;
    --green-light: #b9dc78;
    --charcoal: #4b4b4d;
    --charcoal-dark: #3d3d3f;
    --paper: #e4e5e6;
    --card: #f4f4f4;
    --ink: #3a3a3a;
    --ink-soft: #6a6a6a;
    --white: #ffffff;
  }
  * { box-sizing: border-box; margin: 0; padding: 0; }
  html, body { width: 770px; height: 1200px; overflow: hidden; background: var(--white); }
  .flyer {
    position: relative; width: 770px; height: 1200px; overflow: hidden;
    background: var(--paper);
    font-family: "Arimo", Arial, sans-serif; color: var(--ink);
  }
  .hero-photo {
    position: absolute; left: 0; top: 0; width: 770px; height: 372px;
    background:
      radial-gradient(ellipse 260px 200px at 300px 230px, rgba(150,160,175,0.55) 0%, rgba(150,160,175,0) 100%),
      linear-gradient(180deg, #bcd9ea 0%, #d8e9f1 40%, #d9e4d2 68%, #a9cc6e 100%);
  }
  .brand-banner { position: absolute; right: 0; top: 0; width: 310px; height: 116px; }
  .brand-banner svg { position: absolute; inset: 0; }
  .brand-name {
    position: absolute; left: 40px; right: 0; top: 16px;
    text-align: center; color: var(--white);
    font-weight: 700; font-size: 32px; line-height: 38px;
  }
  .tagline-band {
    position: absolute; left: 0; top: 366px; width: 770px; height: 72px;
    background: var(--green-light);
    border-top: 6px solid var(--green);
  }
  .tagline {
    position: absolute; left: 148px; top: 8px; width: 480px;
    color: var(--white); font-weight: 700; font-size: 21px; line-height: 26px;
  }
  .headline-band {
    position: absolute; left: 0; top: 444px; width: 770px; height: 82px;
    background: var(--charcoal);
  }
  .headline-band svg { position: absolute; inset: 0; }
  .headline {
    position: absolute; left: 106px; top: 6px;
    color: var(--white); font-weight: 700; font-size: 34px; line-height: 36px;
  }
  .photo { position: absolute; top: 526px; height: 186px; }
  .photo-left { left: 48px; width: 300px; background: linear-gradient(135deg, #f1e4d8 0%, #d9c4b2 60%, #b6a99e 100%); }
  .photo-right { left: 410px; width: 294px; background: linear-gradient(135deg, #c9b6a6 0%, #e3d3c6 50%, #a89383 100%); }
  .section-tab { position: absolute; top: 712px; height: 50px; }
  .section-tab svg { position: absolute; inset: 0; }
  .section-tab h2 {
    position: relative; text-align: center; color: var(--white);
    font-weight: 700; font-size: 23px; line-height: 50px; padding-right: 20px;
  }
  .tab-why { left: 48px; width: 324px; }
  .tab-loan { left: 410px; width: 324px; }
  .benefit-card {
    position: absolute; top: 762px; height: 278px; background: var(--card);
    padding: 14px 14px 0 18px;
  }
  .card-why { left: 58px; width: 302px; }
  .card-loan { left: 410px; width: 300px; }
  .benefit-list { list-style: none; }
  .benefit-list li {
    position: relative; padding-left: 30px; margin-bottom: 12px;
    font-family: "PT Serif", Georgia, serif; font-size: 18.5px; line-height: 21px; color: var(--ink);
    text-align: justify; hyphens: auto;
  }
  .benefit-list li svg { position: absolute; left: 0; top: 1px; width: 22px; height: 20px; }
  .cta-line {
    position: absolute; left: 0; top: 1058px; width: 770px; text-align: center;
    font-weight: 700; font-size: 22px; color: var(--ink);
  }
  .cta-phone {
    position: absolute; left: 0; top: 1088px; width: 770px; text-align: center;
    font-weight: 700; font-size: 29px; color: var(--ink-soft);
  }
  .footer-bar {
    position: absolute; left: 0; top: 1124px; width: 770px; height: 76px;
    background: var(--charcoal-dark);
  }
  .contact-labels {
    position: absolute; left: 58px; top: 5px; color: var(--white);
    font-size: 18px; line-height: 22px;
  }
  .footer-brand {
    position: absolute; right: 34px; top: 6px; text-align: center; color: var(--white);
    font-weight: 700; font-size: 29px; line-height: 32px;
  }
</style>
</head>
<body>
<div class="flyer">

  <div class="hero-photo" role="img" aria-label="Photo of a smiling senior couple riding bicycles outdoors"></div>

  <div class="brand-banner">
    <svg width="310" height="116" viewBox="0 0 310 116">
      <polygon points="0,0 310,0 310,116 34,116 34,58" fill="var(--green-light)"/>
      <polygon points="14,0 310,0 310,108 44,108 44,58" fill="var(--green)"/>
    </svg>
    <div class="brand-name">Tamberlyn<br>Funding Corp.</div>
  </div>

  <div class="tagline-band">
    <p class="tagline">Say Goodby to monthly payments<br>with a reverse mortgage</p>
  </div>

  <div class="headline-band">
    <svg width="770" height="82" viewBox="0 0 770 82">
      <polygon points="0,0 44,0 24,41 44,82 0,82" fill="var(--green)"/>
      <polygon points="0,6 30,6 12,41 30,76 0,76" fill="var(--green-light)"/>
      <polygon points="770,0 700,0 680,41 700,82 770,82" fill="var(--green)"/>
      <polygon points="770,6 714,6 696,41 714,76 770,76" fill="var(--green-light)"/>
    </svg>
    <h1 class="headline">Solutions for seniors...<br>Stop worrying Start Living</h1>
  </div>

  <div class="photo photo-left" role="img" aria-label="Photo of a smiling senior man with a caregiver"></div>
  <div class="photo photo-right" role="img" aria-label="Photo of a happy group of seniors giving thumbs up"></div>

  <div class="section-tab tab-why">
    <svg width="324" height="50" viewBox="0 0 324 50"><polygon points="0,0 300,0 324,25 300,50 0,50" fill="var(--green)"/></svg>
    <h2>Why Us</h2>
  </div>
  <div class="section-tab tab-loan">
    <svg width="324" height="50" viewBox="0 0 324 50"><polygon points="0,0 300,0 324,25 300,50 0,50" fill="var(--green)"/></svg>
    <h2>The Loan That Pays You</h2>
  </div>

  <div class="benefit-card card-why">
    <ul class="benefit-list">
      <li><svg viewBox="0 0 22 20"><path d="M2 11 L8 17 L20 2" fill="none" stroke="var(--green)" stroke-width="3.5" stroke-linecap="round" stroke-linejoin="round"/></svg>No Celebrity endorsers or talking heads here.</li>
      <li><svg viewBox="0 0 22 20"><path d="M2 11 L8 17 L20 2" fill="none" stroke="var(--green)" stroke-width="3.5" stroke-linecap="round" stroke-linejoin="round"/></svg>Secure your retirement with a reverse mortgage.</li>
      <li><svg viewBox="0 0 22 20"><path d="M2 11 L8 17 L20 2" fill="none" stroke="var(--green)" stroke-width="3.5" stroke-linecap="round" stroke-linejoin="round"/></svg>GKP Goverment Insured.</li>
      <li><svg viewBox="0 0 22 20"><path d="M2 11 L8 17 L20 2" fill="none" stroke="var(--green)" stroke-width="3.5" stroke-linecap="round" stroke-linejoin="round"/></svg>Retain Complete ownership of your Home.</li>
      <li><svg viewBox="0 0 22 20"><path d="M2 11 L8 17 L20 2" fill="none" stroke="var(--green)" stroke-width="3.5" stroke-linecap="round" stroke-linejoin="round"/></svg>Save and effective financial tool.</li>
    </ul>
  </div>

  <div class="benefit-card card-loan">
    <ul class="benefit-list">
      <li><svg viewBox="0 0 22 20"><path d="M2 11 L8 17 L20 2" fill="none" stroke="var(--green)" stroke-width="3.5" stroke-linecap="round" stroke-linejoin="round"/></svg>Pay Off Credit cards eliminate mortgage payments improve your home or lifestyle.</li>
      <li><svg viewBox="0 0 22 20"><path d="M2 11 L8 17 L20 2" fill="none" stroke="var(--green)" stroke-width="3.5" stroke-linecap="round" stroke-linejoin="round"/></svg>No Credit score or income requirements.</li>
      <li><svg viewBox="0 0 22 20"><path d="M2 11 L8 17 L20 2" fill="none" stroke="var(--green)" stroke-width="3.5" stroke-linecap="round" stroke-linejoin="round"/></svg>Faceing a foreclosure a reverse mortgage can help.</li>
      <li><svg viewBox="0 0 22 20"><path d="M2 11 L8 17 L20 2" fill="none" stroke="var(--green)" stroke-width="3.5" stroke-linecap="round" stroke-linejoin="round"/></svg>Is a reverse mortgage right for you?</li>
    </ul>
  </div>

  <p class="cta-line">Get the facts from a qualified reverse mortgage originator</p>
  <p class="cta-phone">CALL US: 877-520-6184</p>

  <div class="footer-bar">
    <div class="contact-labels">Address<br>e-mail:<br>Phone: 877-520-6184</div>
    <div class="footer-brand">Tamberlyn<br>Funding Corp.</div>
  </div>

</div>
</body>
</html>
```